Business Card Design

Maple Crest Rentals
Maple Crest Rentals is a high end home rental leasing company that provides exquisite properties in niche markets. We are a small family owned business that considers our clients not as renters, but as friends. Every property we buy must be brought up to our high standards before it is offered on the market. The properties that we lease are exceptional, "move in" ready homes. This allows for the client to take pride in their lease as if it was their own home. To put it another way; we do not lease a property that we would not live in ourselves.

Target Market(s)

Couples making $100K or more

Industry/Entity Type

Business

Requirements
Must have
• Some sort of logo
Nice to have
• good slogan
Should not have
• Pink

```html
<!DOCTYPE html>
<html lang="en">
<head>
<meta charset="utf-8">
<title>Maple Crest Rentals — Business Card</title>
<link rel="stylesheet" href="https://fonts.googleapis.com/css2?family=Open+Sans:wght@400;600&display=swap">
<style>
  :root {
    --backdrop: #d9dcda;
    --card: #f7f7f7;
    --card-shade: #e9e9e9;
    --ink: #3c3c3c;
    --ink-soft: #5a5a5a;
    --brand-blue: #1c4f86;
  }
  html, body {
    margin: 0;
    width: 1200px;
    height: 900px;
    overflow: hidden;
    background: var(--backdrop);
    font-family: "Open Sans", Arial, sans-serif;
  }
  .canvas {
    position: relative;
    width: 1200px;
    height: 900px;
  }
  .card {
    position: absolute;
    left: 180px;
    top: 210px;
    width: 840px;
    height: 480px;
    background: linear-gradient(160deg, #ffffff 0%, var(--card) 55%, var(--card-shade) 100%);
    box-shadow: 0 10px 28px rgba(0,0,0,0.22);
    overflow: hidden;
  }
  .accent-shape {
    position: absolute;
    left: 0;
    top: 0;
  }
  .brand {
    position: absolute;
    right: 80px;
    top: 128px;
    display: flex;
    align-items: center;
    gap: 12px;
  }
  .brand-mark {
    width: 18px;
    height: 18px;
    background: var(--brand-blue);
  }
  .brand-name {
    font-size: 28px;
    font-weight: 600;
    color: var(--brand-blue);
    letter-spacing: 0.2px;
  }
  .person {
    position: absolute;
    left: 70px;
    top: 225px;
  }
  .person-name {
    margin: 0;
    font-size: 36px;
    font-weight: 600;
    color: var(--ink);
    line-height: 1;
  }
  .person-title {
    margin: 4px 0 0;
    font-size: 13px;
    color: var(--ink-soft);
    text-align: right;
  }
  .contact {
    position: absolute;
    left: 70px;
    top: 330px;
    margin: 0;
    padding: 0;
    list-style: none;
    font-size: 13px;
    color: var(--ink-soft);
  }
  .contact li {
    display: flex;
    align-items: center;
    gap: 12px;
    height: 20px;
  }
  .contact svg {
    width: 12px;
    height: 12px;
    fill: var(--ink-soft);
    flex: none;
  }
  .contact .no-icon { padding-left: 24px; }
</style>
</head>
<body>
<main class="canvas">
  <section class="card" aria-label="Business card">
    <svg class="accent-shape" width="840" height="480" viewBox="0 0 840 480" aria-hidden="true">
      <polygon points="410,230 610,340 610,420 420,480 410,480" fill="var(--brand-blue)"/>
    </svg>

    <div class="brand">
      <span class="brand-mark"></span>
      <span class="brand-name">Maple Crest Rentals</span>
    </div>

    <div class="person">
      <h1 class="person-name">Daniel Reed</h1>
      <p class="person-title">general manager</p>
    </div>

    <ul class="contact">
      <li>
        <svg viewBox="0 0 12 12"><rect x="3" y="0.5" width="6" height="11" rx="1.2"/></svg>
        555 210 4788
      </li>
      <li>
        <svg viewBox="0 0 12 12"><rect x="0.5" y="2.5" width="11" height="7" rx="1"/></svg>
        dreed@maplecrestrentals.com
      </li>
      <li>
        <svg viewBox="0 0 12 12"><path d="M6 0.5a4 4 0 0 1 4 4c0 3-4 7-4 7s-4-4-4-7a4 4 0 0 1 4-4z"/></svg>
        address line 01
      </li>
      <li class="no-icon">address line 02</li>
    </ul>
  </section>
</main>
</body>
</html>
```